Email Signiture and letterhead design

we are looking for a modern business design to incorporate our logo and qel certification plus social icons for Vorlant, Pelmora, and zandoro
they must include our UK vat and also company registration as text but I can fill these out. Email signature to have a link/icon to our webshop www.trexolan.co.uk

Target Market(s)

All

Font styles to use
Serif
Sans Serif

Requirements
Must have
• Address, tel, email , web details incorperated
Nice to have
• a professional looking letter head and email signiture, Email signature to have a link/icon to our webshop www.trexolan.co.uk

```html
<!DOCTYPE html>
<html lang="en">
<head>
<meta charset="utf-8">
<title>Trexolan Bearings Ltd – Letterhead and Email Signature</title>
<link href="https://fonts.googleapis.com/css2?family=Poppins:wght@400;500;600;700&display=swap" rel="stylesheet">
<style>
  :root {
    --brand-red: #e31e24;
    --brand-dark: #3a3a3a;
    --ink: #2b2b2b;
    --paper: #ffffff;
    --backdrop: #efedea;
    --badge-pink: #e5197e;
    --rule-grey: #d9d9d9;
    --faint-red: #fbe3e4;
  }
  * { box-sizing: border-box; margin: 0; padding: 0; }
  html, body { width: 1200px; height: 3366px; overflow: hidden; }
  body {
    position: relative;
    background: var(--paper);
    font-family: 'Poppins', sans-serif;
    color: var(--ink);
  }

  .presentation {
    position: absolute; left: 0; top: 0;
    width: 1200px; height: 1307px;
    background: var(--backdrop);
  }
  .presentation .sheet-holder {
    position: absolute; left: 204px; top: 94px;
    transform: scale(0.85); transform-origin: top left;
  }

  .letterhead {
    position: relative;
    width: 932px; height: 1318px;
    background: var(--paper);
    box-shadow: 0 8px 30px rgba(0,0,0,0.14);
    overflow: hidden;
  }
  .letterhead-flat { position: absolute; left: 133px; top: 1500px; }

  .header-art { position: absolute; left: 0; top: 0; width: 932px; height: 170px; }
  .footer-art { position: absolute; left: 0; bottom: 0; width: 932px; height: 50px; }

  .brand-name {
    position: absolute;
    font-weight: 600; color: var(--brand-dark);
    letter-spacing: 0.5px; white-space: nowrap;
  }
  .brand-dot { position: absolute; border-radius: 50%; background: var(--brand-red); }

  .contact-line {
    position: absolute; display: flex; align-items: center; gap: 8px;
    font-weight: 600; color: var(--brand-dark); white-space: nowrap;
  }
  .contact-line svg { flex: none; }

  .social-row { position: absolute; display: flex; }
  .social-dot { border-radius: 50%; background: var(--brand-red); }

  .cert-badge {
    position: absolute;
    border: 1.5px solid #bdbdbd; border-radius: 8px;
    background: #fafafa; overflow: hidden;
  }
  .cert-badge .band {
    position: absolute; right: 0; top: 0; bottom: 0; background: var(--badge-pink);
  }
  .cert-badge .bar {
    position: absolute; height: 5px; border-radius: 3px; background: #cfcfcf;
  }
  .cert-number { position: absolute; font-size: 9px; color: #555; white-space: nowrap; }

  .letter-body { position: absolute; left: 82px; top: 289px; width: 771px; }
  .salutation { font-size: 17px; }
  .recipient { font-size: 17px; font-weight: 600; margin: 4px 0 0 5px; }
  .letter-body p {
    font-size: 15.2px; line-height: 19px; text-align: justify;
    margin-top: 36px; color: #333;
  }
  .letter-body p:first-of-type { margin-top: 46px; }
  .sign-off { font-size: 17px; font-weight: 600; margin: 44px 0 0 5px; }

  .faint-mark {
    position: absolute; left: 577px; top: 1053px;
    width: 200px; height: 200px; border-radius: 50%; background: var(--faint-red);
  }

  .signature {
    position: absolute; left: 107px; top: 2960px;
    width: 958px; height: 239px;
    background: var(--paper);
    box-shadow: 0 8px 30px rgba(0,0,0,0.12);
    overflow: hidden;
  }
  .signature-art { position: absolute; left: 0; top: 0; width: 958px; height: 239px; }
  .signature .divider {
    position: absolute; left: 749px; top: 58px; width: 1px; height: 142px; background: var(--rule-grey);
  }
  .signature .faint-mark { left: 858px; top: -60px; width: 110px; height: 110px; }
  .address { font-weight: 500; font-size: 17px; line-height: 21px; }
</style>
</head>
<body>

<section class="presentation">
  <div class="sheet-holder">
    <article class="letterhead">
      <svg class="header-art" viewBox="0 0 932 170" aria-hidden="true">
        <rect x="430" y="0" width="502" height="4" fill="#e31e24"/>
        <path d="M0 154 L318 154 C350 154 362 140 374 112 L410 32 C420 10 428 3 440 3" stroke="#3a3a3a" stroke-width="5" fill="none"/>
        <path d="M322 162 L340 162 C372 162 384 146 396 116 L430 34 C440 12 448 3 462 3" stroke="#e31e24" stroke-width="6" fill="none"/>
      </svg>
      <span class="brand-dot" style="left:230px;top:66px;width:26px;height:26px"></span>
      <span class="brand-name" style="left:43px;top:98px;font-size:21px">TREXOLAN BEARINGS LTD</span>
      <div class="contact-line" style="left:438px;top:38px;font-size:25px">
        <svg width="16" height="16" viewBox="0 0 24 24"><path d="M6.6 10.8a15 15 0 0 0 6.6 6.6l2.2-2.2c.3-.3.7-.4 1-.2 1.1.4 2.3.6 3.6.6.6 0 1 .4 1 1V20c0 .6-.4 1-1 1A17 17 0 0 1 3 4c0-.6.4-1 1-1h3.5c.6 0 1 .4 1 1 0 1.3.2 2.5.6 3.6.1.3 0 .7-.2 1z" fill="#e31e24"/></svg>0161 555 0192
      </div>
      <div class="contact-line" style="left:438px;top:71px;font-size:20px">
        <svg width="16" height="16" viewBox="0 0 24 24"><circle cx="12" cy="12" r="10" fill="#e31e24"/><path d="M2 12h20M12 2c3 3 3 17 0 20M12 2c-3 3-3 17 0 20" stroke="#fff" stroke-width="1.5" fill="none"/></svg>www.trexolan.co.uk
      </div>
      <div class="social-row" style="left:438px;top:111px;gap:10px">
        <span class="social-dot" style="width:18px;height:18px"></span>
        <span class="social-dot" style="width:18px;height:18px"></span>
        <span class="social-dot" style="width:18px;height:18px"></span>
      </div>
      <div class="cert-badge" style="left:690px;top:46px;width:180px;height:62px">
        <span class="bar" style="left:10px;top:12px;width:120px"></span>
        <span class="bar" style="left:10px;top:30px;width:60px"></span>
        <span class="bar" style="left:84px;top:30px;width:50px"></span>
        <span class="bar" style="left:84px;top:42px;width:50px"></span>
        <span class="band" style="width:22px"></span>
      </div>
      <span class="cert-number" style="left:732px;top:112px">Certificate No:480215736</span>

      <div class="letter-body">
        <div class="salutation">To</div>
        <div class="recipient">Lorem Ipsum</div>
        <p>Lorem Ipsum is simply dummy text of the printing and typesetting industry. Lorem Ipsum has been the industry's standard dummy text ever since the 1500s, when an unknown printer took a galley of type and scrambled it to make a type specimen book. It has survived not only five centuries, but also the leap into electronic typesetting, remaining essentially unchanged. It was popularised in the 1960s with the release of Quillmark sheets containing Lorem Ipsum passages, and more recently with desktop publishing software like Norvik PageSetter including versions of Lorem Ipsum.</p>
        <p>Lorem Ipsum is simply dummy text of the printing and typesetting industry. Lorem Ipsum has been the industry's standard dummy text ever since the 1500s, when an unknown printer took a galley of type and scrambled it to make a type specimen book. It has survived not only five centuries, but also the leap into electronic typesetting, remaining essentially unchanged. It was popularised in the 1960s with the release of Quillmark sheets containing Lorem Ipsum passages, and more recently with desktop publishing software like Norvik PageSetter including versions of Lorem Ipsum.</p>
        <p>Lorem Ipsum is simply dummy text of the printing and typesetting industry. Lorem Ipsum has been the industry's standard dummy text ever since the 1500s, when an unknown printer took a galley of type and scrambled it to make a type specimen book. It has survived not only five centuries, but also the leap into electronic typesetting, remaining essentially unchanged. It was popularised in the 1960s with the release of Quillmark sheets containing Lorem Ipsum passages, and more recently with desktop publishing software like Norvik PageSetter including versions of Lorem Ipsum.</p>
        <p>Lorem Ipsum is simply dummy text of the printing and typesetting industry. Lorem Ipsum has been the industry's standard dummy text ever since the 1500s, when an unknown printer took a galley of type and scrambled it to make a type specimen book. It has survived not only five centuries, but also the leap into electronic typesetting, remaining essentially unchanged. It was popularised in the 1960s with the release of Quillmark sheets containing Lorem Ipsum passages, and more recently with desktop publishing software like Norvik PageSetter including versions of Lorem Ipsum.</p>
        <div class="sign-off">Lorem Ipsum</div>
      </div>

      <span class="faint-mark"></span>
      <svg class="footer-art" viewBox="0 0 932 50" aria-hidden="true">
        <polygon points="0,8 160,8 198,42 0,42" fill="#3a3a3a"/>
        <rect x="190" y="28" width="742" height="3" fill="#e31e24"/>
        <rect x="200" y="36" width="732" height="14" fill="#e31e24"/>
      </svg>
    </article>
  </div>
</section>

<article class="letterhead letterhead-flat">
  <svg class="header-art" viewBox="0 0 932 170" aria-hidden="true">
    <rect x="430" y="0" width="502" height="4" fill="#e31e24"/>
    <path d="M0 154 L318 154 C350 154 362 140 374 112 L410 32 C420 10 428 3 440 3" stroke="#3a3a3a" stroke-width="5" fill="none"/>
    <path d="M322 162 L340 162 C372 162 384 146 396 116 L430 34 C440 12 448 3 462 3" stroke="#e31e24" stroke-width="6" fill="none"/>
  </svg>
  <span class="brand-dot" style="left:230px;top:66px;width:26px;height:26px"></span>
  <span class="brand-name" style="left:43px;top:98px;font-size:21px">TREXOLAN BEARINGS LTD</span>
  <div class="contact-line" style="left:438px;top:38px;font-size:25px">
    <svg width="16" height="16" viewBox="0 0 24 24"><path d="M6.6 10.8a15 15 0 0 0 6.6 6.6l2.2-2.2c.3-.3.7-.4 1-.2 1.1.4 2.3.6 3.6.6.6 0 1 .4 1 1V20c0 .6-.4 1-1 1A17 17 0 0 1 3 4c0-.6.4-1 1-1h3.5c.6 0 1 .4 1 1 0 1.3.2 2.5.6 3.6.1.3 0 .7-.2 1z" fill="#e31e24"/></svg>0161 555 0192
  </div>
  <div class="contact-line" style="left:438px;top:71px;font-size:20px">
    <svg width="16" height="16" viewBox="0 0 24 24"><circle cx="12" cy="12" r="10" fill="#e31e24"/><path d="M2 12h20M12 2c3 3 3 17 0 20M12 2c-3 3-3 17 0 20" stroke="#fff" stroke-width="1.5" fill="none"/></svg>www.trexolan.co.uk
  </div>
  <div class="social-row" style="left:438px;top:111px;gap:10px">
    <span class="social-dot" style="width:18px;height:18px"></span>
    <span class="social-dot" style="width:18px;height:18px"></span>
    <span class="social-dot" style="width:18px;height:18px"></span>
  </div>
  <div class="cert-badge" style="left:690px;top:46px;width:180px;height:62px">
    <span class="bar" style="left:10px;top:12px;width:120px"></span>
    <span class="bar" style="left:10px;top:30px;width:60px"></span>
    <span class="bar" style="left:84px;top:30px;width:50px"></span>
    <span class="bar" style="left:84px;top:42px;width:50px"></span>
    <span class="band" style="width:22px"></span>
  </div>
  <span class="cert-number" style="left:732px;top:112px">Certificate No:480215736</span>

  <div class="letter-body">
    <div class="salutation">To</div>
    <div class="recipient">Lorem Ipsum</div>
    <p>Lorem Ipsum is simply dummy text of the printing and typesetting industry. Lorem Ipsum has been the industry's standard dummy text ever since the 1500s, when an unknown printer took a galley of type and scrambled it to make a type specimen book. It has survived not only five centuries, but also the leap into electronic typesetting, remaining essentially unchanged. It was popularised in the 1960s with the release of Quillmark sheets containing Lorem Ipsum passages, and more recently with desktop publishing software like Norvik PageSetter including versions of Lorem Ipsum.</p>
    <p>Lorem Ipsum is simply dummy text of the printing and typesetting industry. Lorem Ipsum has been the industry's standard dummy text ever since the 1500s, when an unknown printer took a galley of type and scrambled it to make a type specimen book. It has survived not only five centuries, but also the leap into electronic typesetting, remaining essentially unchanged. It was popularised in the 1960s with the release of Quillmark sheets containing Lorem Ipsum passages, and more recently with desktop publishing software like Norvik PageSetter including versions of Lorem Ipsum.</p>
    <p>Lorem Ipsum is simply dummy text of the printing and typesetting industry. Lorem Ipsum has been the industry's standard dummy text ever since the 1500s, when an unknown printer took a galley of type and scrambled it to make a type specimen book. It has survived not only five centuries, but also the leap into electronic typesetting, remaining essentially unchanged. It was popularised in the 1960s with the release of Quillmark sheets containing Lorem Ipsum passages, and more recently with desktop publishing software like Norvik PageSetter including versions of Lorem Ipsum.</p>
    <p>Lorem Ipsum is simply dummy text of the printing and typesetting industry. Lorem Ipsum has been the industry's standard dummy text ever since the 1500s, when an unknown printer took a galley of type and scrambled it to make a type specimen book. It has survived not only five centuries, but also the leap into electronic typesetting, remaining essentially unchanged. It was popularised in the 1960s with the release of Quillmark sheets containing Lorem Ipsum passages, and more recently with desktop publishing software like Norvik PageSetter including versions of Lorem Ipsum.</p>
    <div class="sign-off">Lorem Ipsum</div>
  </div>

  <span class="faint-mark"></span>
  <svg class="footer-art" viewBox="0 0 932 50" aria-hidden="true">
    <polygon points="0,8 160,8 198,42 0,42" fill="#3a3a3a"/>
    <rect x="190" y="28" width="742" height="3" fill="#e31e24"/>
    <rect x="200" y="36" width="732" height="14" fill="#e31e24"/>
  </svg>
</article>

<article class="signature">
  <span class="faint-mark"></span>
  <svg class="signature-art" viewBox="0 0 958 239" aria-hidden="true">
    <path d="M300 0 C345 40 356 110 332 168 C320 198 306 220 290 239" stroke="#3a3a3a" stroke-width="6" fill="none"/>
    <path d="M326 0 C376 52 374 150 324 204 C304 225 288 234 270 239" stroke="#e31e24" stroke-width="8" fill="none"/>
    <rect x="280" y="233" width="530" height="6" fill="#e31e24"/>
    <polygon points="808,239 830,215 958,215 958,239" fill="#3a3a3a"/>
  </svg>
  <span class="brand-dot" style="left:228px;top:104px;width:28px;height:28px"></span>
  <span class="brand-name" style="left:23px;top:136px;font-size:21px">TREXOLAN BEARINGS LTD</span>

  <div class="contact-line" style="left:408px;top:62px;font-size:33px;gap:12px">
    <svg width="22" height="22" viewBox="0 0 24 24"><path d="M6.6 10.8a15 15 0 0 0 6.6 6.6l2.2-2.2c.3-.3.7-.4 1-.2 1.1.4 2.3.6 3.6.6.6 0 1 .4 1 1V20c0 .6-.4 1-1 1A17 17 0 0 1 3 4c0-.6.4-1 1-1h3.5c.6 0 1 .4 1 1 0 1.3.2 2.5.6 3.6.1.3 0 .7-.2 1z" fill="none" stroke="#e31e24" stroke-width="2"/></svg>0161 555 0192
  </div>
  <div class="contact-line address" style="left:408px;top:110px;gap:16px;align-items:flex-start">
    <svg width="20" height="24" viewBox="0 0 24 28" style="margin-top:2px"><path d="M12 2a8 8 0 0 0-8 8c0 6 8 14 8 14s8-8 8-14a8 8 0 0 0-8-8z" fill="none" stroke="#e31e24" stroke-width="2"/><circle cx="12" cy="10" r="3" fill="#e31e24"/></svg>
    <span>Larkfield Road North, Ashbury,<br>Manchester, M99 1ZQ</span>
  </div>
  <div class="contact-line" style="left:408px;top:171px;font-size:20px;gap:16px">
    <svg width="20" height="20" viewBox="0 0 24 24"><circle cx="12" cy="12" r="10" fill="#e31e24"/><path d="M2 12h20M12 2c3 3 3 17 0 20M12 2c-3 3-3 17 0 20" stroke="#fff" stroke-width="1.5" fill="none"/></svg>www.trexolan.co.uk
  </div>

  <span class="divider"></span>
  <div class="cert-badge" style="left:768px;top:69px;width:165px;height:59px">
    <span class="bar" style="left:10px;top:11px;width:110px"></span>
    <span class="bar" style="left:10px;top:28px;width:55px"></span>
    <span class="bar" style="left:78px;top:28px;width:45px"></span>
    <span class="bar" style="left:78px;top:40px;width:45px"></span>
    <span class="band" style="width:20px"></span>
  </div>
  <span class="cert-number" style="left:802px;top:133px">Certificate No:480215736</span>
  <div class="social-row" style="left:798px;top:160px;gap:13px">
    <span class="social-dot" style="width:24px;height:24px"></span>
    <span class="social-dot" style="width:24px;height:24px"></span>
    <span class="social-dot" style="width:24px;height:24px"></span>
  </div>
</article>

</body>
</html>
```